Business needs Office Posters Designed

I need a office poster designed to put on a 2 feet x 3 feet space:
My Employee is Better Than Me.
- to signify the importance of listening to your employees, because they know better, more experienced in their respective fields.

Target Market(s)

employees

Industry/Entity Type

Healthcare

```html
<!DOCTYPE html>
<html lang="en">
<head>
<meta charset="UTF-8">
<title>My Employee Is Better Than Me – Office Poster</title>
<link href="https://fonts.googleapis.com/css2?family=Mystery+Quest&family=Raleway:wght@300&display=swap" rel="stylesheet">
<style>
  :root {
    --page-bg: #3a3b3c;
    --poster-dark: #140c22;
    --deep-blue: #1a1f6e;
    --violet: #3b1d5e;
    --amber: #f0a21e;
    --gold: #f6cf3a;
    --leaf: #3e8c4a;
    --ember: #e2402e;
    --crimson: #b0123f;
    --ink-white: #ffffff;
    --turquoise: #33e6d3;
    --orange: #f2b01b;
  }
  * { margin: 0; padding: 0; box-sizing: border-box; }
  html, body {
    width: 1078px;
    height: 1200px;
    overflow: hidden;
    background: var(--page-bg);
  }
  .poster {
    position: absolute;
    left: 155px;
    top: 25px;
    width: 768px;
    height: 1150px;
    overflow: hidden;
    background: var(--poster-dark);
  }
  .poster__glow {
    position: absolute;
    inset: 0;
    background:
      radial-gradient(ellipse 28% 20% at 50% 52%, rgba(10,12,20,0.95) 0%, rgba(10,12,20,0.75) 60%, rgba(10,12,20,0) 100%),
      radial-gradient(ellipse 58% 42% at 50% 50%, rgba(62,140,74,0.55) 0%, rgba(240,162,30,0.9) 45%, rgba(246,207,58,0.0) 80%),
      radial-gradient(ellipse 70% 30% at 45% 78%, rgba(226,64,46,0.9) 0%, rgba(176,18,63,0.75) 50%, rgba(176,18,63,0) 100%),
      radial-gradient(ellipse 60% 30% at 70% 20%, rgba(240,162,30,0.8) 0%, rgba(240,162,30,0) 100%),
      linear-gradient(180deg, var(--deep-blue) 0%, var(--violet) 35%, var(--crimson) 72%, var(--poster-dark) 100%);
  }
  .poster__echo {
    position: absolute;
    left: 0;
    width: 100%;
    font-family: 'Raleway', sans-serif;
    font-weight: 300;
    color: rgba(255,255,255,0.35);
    filter: blur(5px);
    white-space: nowrap;
    line-height: 1;
  }
  .poster__echo--top { top: 70px; left: 195px; font-size: 230px; }
  .poster__echo--mid1 { top: 330px; left: -30px; font-size: 200px; color: rgba(255,255,255,0.18); }
  .poster__echo--mid2 { top: 560px; left: -40px; font-size: 200px; color: rgba(255,255,255,0.18); }
  .poster__echo--bottom { top: 860px; left: 185px; font-size: 230px; }
  .headline {
    position: absolute;
    inset: 0;
    font-family: 'Mystery Quest', cursive;
    font-size: 122px;
    line-height: 140px;
  }
  .headline__line {
    position: absolute;
    white-space: nowrap;
    transform: rotate(-9deg);
    transform-origin: left center;
    text-shadow: 0 0 10px rgba(0,0,0,0.35);
  }
  .headline__line--my { left: 310px; top: 342px; }
  .headline__line--employee { left: 65px; top: 517px; }
  .headline__line--better { left: 85px; top: 632px; }
  .headline__line--me { left: 305px; top: 702px; }
  .word--white { color: var(--ink-white); }
  .word--turquoise { color: var(--turquoise); }
  .word--orange { color: var(--orange); }
</style>
</head>
<body>
  <main class="poster">
    <div class="poster__glow" role="img" aria-label="Blurred bokeh of glowing sparkles in blue, gold, green and red around a dark centre"></div>
    <div class="poster__echo poster__echo--top" aria-hidden="true">My</div>
    <div class="poster__echo poster__echo--mid1" aria-hidden="true">employee</div>
    <div class="poster__echo poster__echo--mid2" aria-hidden="true">better than</div>
    <div class="poster__echo poster__echo--bottom" aria-hidden="true">Me</div>
    <h1 class="headline">
      <span class="headline__line headline__line--my word--white">my</span>
      <span class="headline__line headline__line--employee"><span class="word--white">employee</span> <span class="word--turquoise">is</span></span>
      <span class="headline__line headline__line--better word--turquoise">better than</span>
      <span class="headline__line headline__line--me word--orange">me</span>
    </h1>
  </main>
</body>
</html>
```